Hollow Lantern Town Strolling Past Tour

We are launching a different kind of city historical walking tour company with a slightly darker approach using historical but real stories that have long been forgotten from living memory.
Our tour is going to contain a lot of very thoroughly researched stories ranging from 50 to 150 years past that takes the customer into the actual-real life past of the city streets.  Stories that may contains some dark undertones and stories with a twist or that seem eccentric to us now but were entirely normal back in olden times - minus the dry historical facts that most tours engage in..
Our tours are going to run both day and night and will incorporate real history / real Hollow Lantern, so some of the stories will be quite serious (e.g.- there are actual murders from 100 years ago, baffling court cases, even a bit of poetry written by murderers, suicides, love triangles, you name it.  We are aiming for a mystery/history theme and are aiming to attract tourists who are interested in getting a different kind of history.

We're not going for scares and even though we expect people to enjoy our tours;  we're not aiming at light fun and frivolity.  I guess if you wanted to give us a tv rating we'd be aiming at M to MA15+.
If I was to give you another analogy using the literature world.  Think Edwin Harrowgates Nightwarden rather than the Moonveil Saga of movies.  Or Agnes Pellowe's Corvanthus rather than the Grimbles.  Even Crown of Embers rather than a soap opera.
Our stories are being carefully crafted and are packed with unexpected twists, turns & revelations whilst remaining all 100% true.  We have approx 15-20 stories for each tour and we're designing them in a way that each story will trigger a different range of emotions in the listeners on a regular basis.  We're being very careful to keep it fresh for each story so that it will next to impossible for our guests to zone out!  I personally can't stand going on a tour where mildly interesting facts are read out.  We like deep, rich stories rather than pop entertainment.
We want the website to generate a feeling/atmosphere for our product that draws the right crowd to our tours as well as making it easy to make a booking.  Basic features to include:-
Home Page
Bookings Page
Integration with a booking system will be required here via use of plugin code.
Private Functions Page
We are hoping to integrate with a booking system via use of plugin code.  If not, then a simple form enquiry type input e.g.- name, emails, subject, contact, details, preferred date/time, etc).
About Us Page :-
Dark; a euphemism for the unknown or the forgotten.  Think dark ages, dark matter, dark energy; things where knowledge is uncertain or unknown are often termed dark.   Hollow Lantern brings back the hidden past, the forgotten past, the past that may not want to be remembered……but these are real stories....real stories that come from the streets around you.

Some of these stories may be tales of dark things.....some may simply be a charming reminder of days gone by…..regardless these stories are compelling reminders of the amazing times that precede us…..and the forgotten people of yesteryear finally get a chance to have their story told to a fresh audience.  Through you, the people of yesterday get to live again.  Will you like what you hear?

Contact Us page:-
•	A form input type page.
•	Include space for our phone number
•	Include space for our email address
Other Items:-
Social Media Links; we will be looking for social media icons to link to our social media pages to Friendloop, Snapvista, Chirpline.
Subscription; we want to also capture an input email address box for site visitors.  We will be launching a weekly Hollow Lantern podcast / email newsetter; with a weekly Hollow Lantern from a different place in the world and we want some way for people to subscribe.

Updates
Project Deadline Extended
Reason: A few additional photos have been uploaded.  Feel free to utilize if helpful.  Our stories range from the 1800s to 1950s in an era with beautiful old Victorian buildings.  I'm putting through the extension just to give some more time to see if this gives any more ideas and inspiration.  Thank you for all the great submissions.

Target Market(s)
Tourists that want to hear a darker version of the city they are visiting. Stories that other tour companies would not even think of covering. The real history of the events that ordinary people lived through that didn't necessarily make the history books. All stories are true; as per project description.
Industry/Entity Type
Tourism
Coding
Coded - Design and coding required
Number of Pages Required
5+ page
Colors
Designer to choose colors to be used in the design.
Look and feel

```html
<!DOCTYPE html>
<html lang="en">
<head>
<meta charset="utf-8">
<title>Hollow Lantern — Town Strolling Past Tour</title>
<link rel="stylesheet" href="https://fonts.googleapis.com/css2?family=Lato:wght@400;700&family=Open+Sans:wght@400;600&display=swap">
<style>
:root{
  --red:#c8302f;
  --red-deep:#a3221f;
  --ink:#1c1c1c;
  --muted:#6a6a6a;
  --white:#ffffff;
  --night:#1f2522;
  --sky:#5d7fa4;
}
*{margin:0;padding:0;box-sizing:border-box}
html,body{width:1200px;height:3273px;overflow:hidden;background:var(--white)}
body{position:relative;font-family:"Open Sans",Arial,sans-serif;color:var(--ink)}
.abs{position:absolute}
.heading{font-family:"Lato",Arial,sans-serif;font-weight:400;font-size:40px;color:var(--ink)}
.heading em{font-style:normal;color:var(--red)}
.copy{font-size:13.5px;line-height:25px;color:var(--muted)}
.btn{display:flex;align-items:center;justify-content:center;background:var(--red);color:var(--white);font-family:"Open Sans",Arial,sans-serif;font-size:19px;height:56px;width:188px}

/* header */
.site-header{left:0;top:0;width:1200px;height:110px;background:var(--white)}
.brand{left:86px;top:38px;display:flex;align-items:center;gap:10px;font-family:"Lato",sans-serif;font-weight:700;font-size:18px;color:var(--ink);letter-spacing:.5px}
.brand i{width:26px;height:26px;background:var(--ink);display:block;border-radius:50%}
.main-nav{right:72px;top:42px;display:flex;gap:26px;align-items:center;font-size:16px;color:#444}
.main-nav .active{color:var(--red)}

/* hero */
.hero{left:0;top:110px;width:1200px;height:530px;background:linear-gradient(180deg,#3a557c 0%,#6d86a3 38%,#5b5449 62%,#3b4a52 100%)}
.hero-title{left:0;top:140px;width:1200px;text-align:center;font-family:"Lato",sans-serif;font-size:60px;color:var(--white);letter-spacing:1px}
.hero-title b{font-weight:700}
.hero-sub{left:0;top:218px;width:1200px;text-align:center;font-family:"Open Sans",Arial,sans-serif;font-size:25px;color:var(--white);letter-spacing:.5px}
.hero-btn{left:495px;top:288px;width:210px;height:68px;background:var(--white);color:var(--red);font-size:20px;display:flex;align-items:center;justify-content:center}
.hero-wave{left:0;top:420px}
.badge{left:862px;top:530px;width:260px;height:260px;border-radius:50%;background:var(--ink);border:16px solid var(--red);box-shadow:0 0 0 10px var(--white) inset;display:flex;align-items:center;justify-content:center;color:var(--white);font-family:"Lato",sans-serif;font-weight:700;font-size:24px;text-align:center;line-height:30px}

/* intro */
.intro-title{left:0;top:740px;width:1200px;text-align:center}
.intro-copy{left:230px;top:808px;width:740px;text-align:center}
.intro-btn{left:520px;top:932px}

/* split features */
.feature-img{left:0;width:1200px}
.season-img{top:1063px;height:417px;background:linear-gradient(180deg,#3e83c9 0%,#8fb6da 35%,#8b8f5a 62%,#35482c 100%);clip-path:polygon(0 0,788px 0,650px 100%,0 100%)}
.offer-img{top:1500px;height:418px;background:linear-gradient(180deg,#6b6a80 0%,#e4a44b 40%,#c67c3e 55%,#3c4a66 100%);clip-path:polygon(592px 0,1200px 0,1200px 100%,412px 100%)}
.season-title{left:776px;top:1120px}
.season-copy{left:776px;top:1180px;width:360px}
.season-btn{left:774px;top:1355px}
.offer-title{left:80px;top:1554px}
.offer-copy{left:80px;top:1614px;width:360px}
.offer-btn{left:78px;top:1791px}

/* coming soon */
.soon-title{left:0;top:1972px;width:1200px;text-align:center}
.card{top:2075px;width:333px;height:260px}
.card-a{left:77px;background:linear-gradient(180deg,#6d93c6 0%,#b7a58d 55%,#8b6a4f 100%)}
.card-b{left:434px;background:linear-gradient(180deg,#4c7bc0 0%,#9aa2a2 45%,#7b6a52 100%)}
.card-c{left:790px;background:linear-gradient(180deg,#7fa3cf 0%,#bcbdbd 50%,#7a8062 100%)}
.card-cap{left:0;bottom:0;width:100%;height:73px;background:rgba(200,48,47,.85);color:var(--white);text-align:center;padding-top:8px}
.card-cap small{display:block;font-size:13px}
.card-cap span{display:block;font-family:"Lato",sans-serif;font-size:20px;margin-top:2px}

/* popular */
.popular{left:0;top:2418px;width:1200px;height:437px;background:linear-gradient(180deg,#2b2f2c 0%,#1b231f 60%,#263128 100%)}
.popular-title{left:0;top:2472px;width:1200px;text-align:center;color:var(--white)}
.popular-copy{left:210px;top:2542px;width:780px;text-align:center;color:#e6e6e6}
.place{top:2634px;width:146px;height:146px;border-radius:50%;border:4px solid var(--white)}

/* footer */
.site-footer{left:0;top:2855px;width:1200px;height:418px;background:linear-gradient(180deg,#cf4a3c 0%,#c7392f 50%,#b12b26 100%)}
.foot-col{top:2918px;color:var(--white)}
.foot-col h3{font-family:"Lato",sans-serif;font-weight:400;font-size:19px;margin-bottom:26px}
.foot-col p{font-size:12.5px;line-height:20px}
.col-testimonial{left:80px;width:250px}
.col-contact{left:367px;width:220px}
.col-blog{left:615px;width:250px}
.col-news{left:893px;width:230px}
.arrows{left:282px;top:2913px;display:flex;gap:4px}
.arrows span{width:22px;height:22px;display:flex;align-items:center;justify-content:center;border:1px solid var(--white)}
.arrows span.on{background:var(--ink);border-color:var(--ink)}
.who{display:flex;gap:12px;align-items:center;margin-bottom:14px}
.avatar{width:76px;height:76px;border-radius:50%;background:#d9a48e;border:3px solid var(--white);flex:none}
.who b{font-weight:400;font-size:14px;display:block}
.who i{font-size:12px}
.contact-row{display:flex;gap:14px;margin-bottom:14px}
.contact-row svg{flex:none;margin-top:3px}
.post{display:flex;gap:18px;align-items:center;padding-bottom:12px;margin-bottom:12px;border-bottom:1px solid rgba(255,255,255,.55)}
.post:last-child{border:0}
.thumb{width:72px;height:72px;border-radius:50%;border:2px solid var(--white);background:#4a4640;flex:none}
.post i{display:block;font-size:11.5px;margin-top:2px}
.email-input{margin-top:14px;width:230px;height:46px;background:#f1f1f1;color:#555;font-size:13px;display:flex;align-items:center;padding-left:14px}
.submit{margin-top:10px;width:158px;height:50px;background:#0d0d0d;border:1px solid var(--white);color:var(--white);font-size:20px;display:flex;align-items:center;justify-content:center}
.copyright{left:0;top:3205px;width:1200px;height:68px;border-top:1px solid rgba(255,255,255,.5);background:var(--red-deep);color:var(--white);font-size:13.5px;display:flex;align-items:center;justify-content:center}
</style>
</head>
<body>

<header class="abs site-header">
  <div class="abs brand"><i></i>Hollow Lantern</div>
  <nav class="abs main-nav">
    <span class="active">Home</span><span>About</span><span>Booking</span><span>Private Pakage</span><span>Blog</span><span>Contact</span>
    <svg width="20" height="20" viewBox="0 0 20 20"><circle cx="8" cy="8" r="6" fill="none" stroke="#c8302f" stroke-width="2"/><line x1="12.5" y1="12.5" x2="18" y2="18" stroke="#c8302f" stroke-width="2"/></svg>
  </nav>
</header>

<section class="abs hero" role="img" aria-label="Old town river with gothic church spires under a cloudy evening sky">
  <h1 class="abs hero-title"><b>HOLLOW</b> LANTERN</h1>
  <p class="abs hero-sub">HISTORICAL CONTEMPORARY &amp; EVERYTHING IN BETWEEN</p>
  <div class="abs hero-btn">LEARN MORE</div>
  <svg class="abs hero-wave" width="1200" height="110" viewBox="0 0 1200 110">
    <path d="M0 30 C180 110 340 120 560 80 C780 40 980 0 1200 15 L1200 110 L0 110 Z" fill="#fff"/>
    <path d="M0 30 C180 110 340 120 560 80 C780 40 980 0 1200 15" fill="none" stroke="#c8302f" stroke-width="7"/>
  </svg>
</section>
<div class="abs badge">Hollow<br>Lantern</div>

<h2 class="abs heading intro-title">History about <em>Hollow Lantern</em></h2>
<p class="abs copy intro-copy">Lorem Ipsum is simply dummy text of the printing and typesetting industry. Lorem Ipsum has been the industry's standard dummy text ever since the 1500s, when an unknown printer took a galley of type and scrambled it to make a type specimen book. It has survived not only five centuries, but also the leap into electronic typesetting, remaining essentially unchanged. It was popularised in the 1960s</p>
<div class="abs btn intro-btn">READ MORE</div>

<div class="abs feature-img season-img" role="img" aria-label="Marble statue in front of a palace with terraced gardens under a blue sky"></div>
<h2 class="abs heading season-title">Four <em>This Season</em></h2>
<p class="abs copy season-copy">Lorem Ipsum is simply dummy text of the printing and typesetting industry. Lorem Ipsum has been the industry's standard dummy text ever since the 1500s, when an unknown printer took a galley of type and scrambled it to make a type specimen book. It has survived not only five centuries.</p>
<div class="abs btn season-btn">READ MORE</div>

<div class="abs feature-img offer-img" role="img" aria-label="Whitewashed hillside village with windmills above the sea at sunset"></div>
<h2 class="abs heading offer-title">Best <em>Offers</em></h2>
<p class="abs copy offer-copy">Lorem Ipsum is simply dummy text of the printing and typesetting industry. Lorem Ipsum has been the industry's standard dummy text ever since the 1500s, when an unknown printer took a galley of type and scrambled it to make a type specimen book. It has survived not only five centuries.</p>
<div class="abs btn offer-btn">READ MORE</div>

<h2 class="abs heading soon-title">Comingsoon <em>Season</em></h2>
<div class="abs card card-a" role="img" aria-label="Hot air balloons over rocky valley at dawn"><div class="abs card-cap"><small>Lorem Ipsum is simply dummy</small><span>Lorem Ipsum is simply dummy</span></div></div>
<div class="abs card card-b" role="img" aria-label="Historic city gate topped by a chariot statue"><div class="abs card-cap"><small>Lorem Ipsum is simply dummy</small><span>Lorem Ipsum is simply dummy</span></div></div>
<div class="abs card card-c" role="img" aria-label="Ancient temple columns in front of mountains"><div class="abs card-cap"><small>Lorem Ipsum is simply dummy</small><span>Lorem Ipsum is simply dummy</span></div></div>

<section class="abs popular" role="img" aria-label="Dark lakeside park with trees and boats at dusk"></section>
<h2 class="abs heading popular-title">Your most <em>Popular Places</em></h2>
<p class="abs copy popular-copy">Lorem Ipsum is simply dummy text of the printing and typesetting industry. Lorem Ipsum has been the industry's standard dummy text ever since the 1500s, when an unknown printer took a galley of type and scrambled.</p>
<div class="abs place" style="left:82px;background:linear-gradient(180deg,#6f9bd0,#d8d2c0 60%,#6a8a4a)" role="img" aria-label="Leaning bell tower"></div>
<div class="abs place" style="left:259px;background:linear-gradient(180deg,#7aa6d6,#cfc6b2 55%,#5f7a45)" role="img" aria-label="Triumphal arch"></div>
<div class="abs place" style="left:437px;background:linear-gradient(180deg,#8aaed2,#b59a80 55%,#6e6457)" role="img" aria-label="Seaside stone statue"></div>
<div class="abs place" style="left:614px;background:linear-gradient(180deg,#9bb4cf,#c8bda4 55%,#7c7a64)" role="img" aria-label="Ruined temple columns"></div>
<div class="abs place" style="left:791px;background:linear-gradient(180deg,#c0b6a8,#e2b574 50%,#6b5a46)" role="img" aria-label="City gate at sunset"></div>
<div class="abs place" style="left:969px;background:linear-gradient(180deg,#7ea7d4,#d8c9a8 55%,#a08a68)" role="img" aria-label="Hilltop temple ruins"></div>

<footer class="abs site-footer" role="img" aria-label="Red savanna scene with elephant and tree silhouettes"></footer>

<div class="abs foot-col col-testimonial">
  <h3>Testimonial</h3>
  <div class="who"><div class="avatar" role="img" aria-label="Customer portrait"></div><div><b>MARA QUILL</b><i>Director</i></div></div>
  <p>Lorem Ipsum is simply dummy text of the printing and typesetting industry. Lorem Ipsum has been the industry.</p>
</div>
<div class="abs arrows">
  <span><svg width="10" height="10" viewBox="0 0 10 10"><path d="M7 1 L3 5 L7 9" fill="none" stroke="#fff" stroke-width="2"/></svg></span>
  <span class="on"><svg width="10" height="10" viewBox="0 0 10 10"><path d="M3 1 L7 5 L3 9" fill="none" stroke="#fff" stroke-width="2"/></svg></span>
</div>

<div class="abs foot-col col-contact">
  <h3>Contact Info</h3>
  <div class="contact-row">
    <svg width="14" height="18" viewBox="0 0 14 18"><path d="M7 0 C3 0 0 3 0 7 C0 12 7 18 7 18 C7 18 14 12 14 7 C14 3 11 0 7 0Z" fill="#111"/><circle cx="7" cy="7" r="2.5" fill="#c8302f"/></svg>
    <p>HOLLOW LANTERN<br>101 - Lorem Ipsum is simple dummy text of print &amp; type setting industry.</p>
  </div>
  <div class="contact-row">
    <svg width="16" height="16" viewBox="0 0 16 16"><path d="M3 1 L6 1 L7 5 L5 6 C6 8 8 10 10 11 L11 9 L15 10 L15 13 C15 14 14 15 13 15 C6 15 1 10 1 3 C1 2 2 1 3 1Z" fill="#111"/></svg>
    <p>555-014-2290</p>
  </div>
  <div class="contact-row">
    <svg width="17" height="13" viewBox="0 0 17 13"><rect x="1" y="1" width="15" height="11" fill="none" stroke="#111" stroke-width="2"/><path d="M1 1 L8.5 7 L16 1" fill="none" stroke="#111" stroke-width="2"/></svg>
    <p>hello@hollowlantern.example</p>
  </div>
</div>

<div class="abs foot-col col-blog">
  <h3>BLOG POST</h3>
  <div class="post"><div class="thumb" role="img" aria-label="Blog post thumbnail"></div><p>Lorem Ipsum is simply dummy text of the.<i>18 Nov 2017</i></p></div>
  <div class="post"><div class="thumb" style="background:#55603c" role="img" aria-label="Blog post thumbnail"></div><p>Lorem Ipsum is simply dummy text of the.<i>18 Nov 2017</i></p></div>
</div>

<div class="abs foot-col col-news">
  <h3>Newsletter</h3>
  <p>Would you like to receive exclusive access to articles, white papers and our regular monthly newsletter?</p>
  <div class="email-input">Enter Email Id</div>
  <div class="submit">SUBMIT</div>
</div>

<div class="abs copyright">©&nbsp;&nbsp;<b>HOLLOW LANTERN</b>&nbsp;- 2017. All Rights Reserved.</div>

</body>
</html>
```